Label design for high quality nutritional supplement brand

We need a new label design for our dietary supplement brand "NorlumPlus" from Germany. We sell high-quality nutritional supplements that help improve overall well-being.

All products in our range should receive the new label. You can find our current design on our homepage norlumplus-shop.example. The new design should be completely redesigned and look modern, fresh, high quality, minimalist and clean. We prefer the colors nude, green and earth tones.

The newly created label should contain our NorlumPlus logo. For this reason you will find this file attached. You will also find our current label, which needs to be renewed, in the appendix.

Colors

Designer to choose colors to be used in the design.

Requirements
Must have
• NorlumPlus logo

```html
<!DOCTYPE html>
<html lang="en">
<head>
<meta charset="utf-8">
<title>NorlumPlus Complex Multivitamin Label</title>
<link rel="stylesheet" href="https://fonts.googleapis.com/css2?family=Montserrat:wght@400;500&display=swap">
<style>
  :root {
    --canvas: #e9eaec;
    --label-white: #ffffff;
    --olive: #bcbf2b;
    --olive-deep: #a9ac22;
    --ink: #1c1c1c;
    --ink-soft: #3a3a3a;
    --logo-tone: #9a9d24;
    --dots-light: #f4f5f6;
    --dots-mid: #e6e8eb;
  }
  * { box-sizing: border-box; margin: 0; padding: 0; }
  html, body {
    width: 1200px;
    height: 1200px;
    overflow: hidden;
    background: var(--canvas);
    font-family: "Montserrat", sans-serif;
  }
  .label {
    position: absolute;
    left: 160px;
    top: 40px;
    width: 880px;
    height: 1120px;
    background: var(--label-white);
    overflow: hidden;
  }
  .label__top-band {
    position: absolute;
    left: 0; top: 0;
    width: 100%;
    height: 48px;
    background: linear-gradient(90deg, var(--olive-deep), var(--olive) 50%, var(--olive-deep));
  }
  .label__pattern {
    position: absolute;
    left: 0; top: 48px;
    width: 100%;
    height: 1072px;
    background:
      linear-gradient(to bottom, rgba(255,255,255,0) 35%, var(--label-white) 75%),
      radial-gradient(ellipse 70% 40% at 65% 32%, var(--dots-mid) 0%, var(--dots-light) 50%, var(--label-white) 100%);
  }
  .brand-mark {
    position: absolute;
    left: 150px;
    top: 320px;
    display: flex;
    align-items: center;
    gap: 22px;
    font-weight: 400;
    font-size: 84px;
    letter-spacing: -1px;
    color: var(--logo-tone);
  }
  .brand-mark__dot {
    width: 30px;
    height: 30px;
    border-radius: 50%;
    background: var(--logo-tone);
  }
  .product-panel {
    position: absolute;
    left: 83px;
    top: 560px;
    width: 690px;
    height: 380px;
    background: var(--olive);
  }
  .product-panel__curl {
    position: absolute;
    right: 0;
    top: 0;
    width: 110px;
    height: 250px;
  }
  .product-panel__name {
    position: absolute;
    left: 100px;
    top: 66px;
    font-size: 76px;
    font-weight: 500;
    color: var(--ink);
    letter-spacing: -0.5px;
    white-space: nowrap;
  }
  .product-panel__variant {
    position: absolute;
    left: 190px;
    top: 180px;
    font-size: 58px;
    font-weight: 400;
    color: var(--label-white);
  }
  .product-panel__type {
    position: absolute;
    left: 135px;
    top: 285px;
    font-size: 50px;
    font-weight: 400;
    color: var(--ink-soft);
    letter-spacing: 1px;
  }
  .web-strip {
    position: absolute;
    left: 83px;
    top: 960px;
    width: 690px;
    height: 66px;
    background: var(--label-white);
    display: flex;
    align-items: center;
    justify-content: center;
    font-size: 36px;
    color: var(--ink);
    white-space: nowrap;
  }
  .label__bottom-band {
    position: absolute;
    left: 83px;
    top: 1036px;
    width: 690px;
    height: 84px;
    background: var(--olive);
  }
</style>
</head>
<body>
  <div class="label">
    <div class="label__top-band"></div>
    <div class="label__pattern" role="img" aria-label="Soft grey dotted wave pattern background"></div>

    <div class="brand-mark">
      <span class="brand-mark__dot"></span>
      <span class="brand-mark__name">NorlumPlus</span>
    </div>

    <div class="product-panel">
      <svg class="product-panel__curl" viewBox="0 0 110 250" aria-hidden="true">
        <path d="M20 0 H110 V250 C85 185 65 120 52 70 C44 35 34 10 20 0 Z" fill="#ffffff"/>
        <path d="M20 0 C34 10 44 35 52 70 C65 120 85 185 110 250" fill="none" stroke="#1c1c1c" stroke-width="7"/>
      </svg>
      <div class="product-panel__name">NorlumPlus</div>
      <div class="product-panel__variant">Complex</div>
      <div class="product-panel__type">Multivitamin</div>
    </div>

    <div class="web-strip">www.norlumplus-shop.example</div>
    <div class="label__bottom-band"></div>
  </div>
</body>
</html>
```